Brochure for a paper wholesaler who wants to educate his print industry clients

We will be making a stapled informative brochure, that contains basic information about our paper products - the types of paper there is, their characteristics and other useful information.
As we are part of a paper wholesaler group in Europe - VORENT, we received a brochure in German that has this kind of information. The text in it is not as important. What is important is the layout of the document and how the text will appear in it (added in the uploaded files - 210915_Wiessenswertes_TBLK_F51.pdf).
We are allowed to tinker with this file and adjust it to our needs. So there are also .idml and .indd files available (also in the uploaded files).
We would like to keep the custom page size of 210 x290mm (8.3x11.4 in), or you can go up to 210x297mm (8.3x11.7 in).
What we want is a modern looking design that contains our companies red bordo and white/ grey colours to replace the existing green colours in this borchure. The pictures and appearance of the file can be changed according to your views and what you think would look good. We don't necessarily want to keep the same design, we just want the layout of the document be the same, as we will be placing our translated text into it. The VORENT logo should be replaced with our own logo (KUMET Logo.png).
As for how it could look, it could go together with our paper presentation, for which the design can be seen in the "KUMET Base - v2.pptx".
Holiday season, so have a lot of tasks to take care of and not as much time to check ArtHarbor as often.

```html
<!DOCTYPE html>
<html lang="de">
<head>
<meta charset="utf-8">
<title>Brochure spread – Fachlatein</title>
<link href="https://fonts.googleapis.com/css2?family=Josefin+Sans:wght@300;400;600;700&display=swap" rel="stylesheet">
<style>
  :root {
    --bg: #a7a7a7;
    --paper: #ffffff;
    --paper-shade: #f1f1f1;
    --bordo: #8b2a32;
    --ink: #4a4a4a;
    --ink-soft: #8a8a8a;
    --rule: #d6d6d6;
  }
  * { box-sizing: border-box; margin: 0; padding: 0; }
  html, body { width: 1200px; height: 900px; overflow: hidden; }
  body {
    background: var(--bg);
    font-family: "Josefin Sans", sans-serif;
    color: var(--ink);
    position: relative;
  }
  .spread {
    position: absolute;
    left: 190px; top: 167px;
    width: 820px; height: 566px;
    display: flex;
    box-shadow: 0 12px 30px rgba(0,0,0,.25);
  }
  .page {
    position: relative;
    width: 410px; height: 566px;
    background: var(--paper);
  }
  .page--left { background: linear-gradient(to right, var(--paper) 85%, var(--paper-shade)); }
  .page--right { background: linear-gradient(to left, var(--paper) 88%, var(--paper-shade)); }

  /* left page */
  .cover-visual {
    position: absolute; left: 0; top: 0;
    width: 100%; height: 300px;
    background:
      radial-gradient(ellipse at 70% 20%, #e8e8e8 0%, rgba(232,232,232,0) 55%),
      linear-gradient(165deg, #6f6f6f 0%, #b9b9b9 35%, #ececec 60%, rgba(255,255,255,0) 100%);
  }
  .gutter-note {
    position: absolute; right: 12px; top: 250px;
    transform: rotate(90deg); transform-origin: right top;
    font-size: 5px; letter-spacing: .5px; color: var(--ink-soft);
    white-space: nowrap;
  }
  .toc {
    position: absolute; left: 36px; top: 322px; width: 180px;
  }
  .toc__bar { width: 24px; height: 2px; background: var(--bordo); margin-bottom: 8px; }
  .toc__title {
    font-size: 17px; font-weight: 600; letter-spacing: 1px;
    color: var(--bordo); margin-bottom: 8px;
  }
  .toc__list { list-style: none; }
  .toc__item {
    display: flex; justify-content: space-between; align-items: flex-end;
    font-size: 7px; font-weight: 600; color: var(--ink);
    border-bottom: 1px solid var(--rule);
    padding: 5px 0 2px;
  }
  .toc__item span:last-child { font-weight: 300; color: var(--ink-soft); }
  .folio { position: absolute; bottom: 18px; font-size: 6px; color: var(--ink-soft); }
  .folio--left { left: 36px; }
  .folio--right { right: 36px; }

  /* right page */
  .content { position: absolute; left: 34px; top: 92px; right: 34px; }
  .content__title {
    font-size: 15px; font-weight: 600; letter-spacing: 1.4px;
    color: var(--bordo); text-transform: uppercase; margin-bottom: 10px;
  }
  .content__lead { font-size: 7px; font-weight: 700; margin-bottom: 10px; }
  .glossary { display: grid; grid-template-columns: 82px 1fr; row-gap: 10px; column-gap: 8px; font-size: 6.5px; line-height: 1.45; }
  .glossary dt { font-weight: 700; }
  .glossary dd { font-weight: 300; color: var(--ink-soft); }
  .abbr { margin-top: 26px; }
  .abbr__title { font-size: 7px; font-weight: 700; margin-bottom: 6px; }
  .abbr__table { width: 100%; border-collapse: collapse; font-size: 6.2px; line-height: 1.3; }
  .abbr__table td { padding: 1.5px 0; vertical-align: top; font-weight: 300; color: var(--ink-soft); }
  .abbr__table td:first-child { width: 62px; font-weight: 700; color: var(--ink); }
  .abbr__table td:nth-child(2) { width: 100px; }
  .brand-name {
    position: absolute; right: 52px; bottom: 18px;
    font-size: 6px; font-weight: 400; color: var(--ink-soft);
  }
  .running-foot { position: absolute; left: 34px; bottom: 18px; font-size: 5.5px; letter-spacing: 1px; color: var(--ink-soft); }
</style>
</head>
<body>
  <div class="spread">
    <section class="page page--left">
      <div class="cover-visual" role="img" aria-label="Abstract image of a softly curling grey paper sheet"></div>
      <p class="gutter-note">Papier und Druck kompakt erklärt</p>
      <nav class="toc">
        <div class="toc__bar"></div>
        <h2 class="toc__title">INHALT</h2>
        <ul class="toc__list">
          <li class="toc__item"><span>Fachlatein für Fortgeschrittene</span><span>03</span></li>
          <li class="toc__item"><span>Karton im Überblick</span><span>04</span></li>
          <li class="toc__item"><span>Das kleine 1x1 der Formatschule</span><span>04</span></li>
          <li class="toc__item"><span>Umfangreiche Sache</span><span>05</span></li>
          <li class="toc__item"><span>Hilfe bei Gewichtsproblemen</span><span>06</span></li>
          <li class="toc__item"><span>Die feine Art zu drucken</span><span>07</span></li>
          <li class="toc__item"><span>Wegweiser für die Laufrichtung</span><span>08</span></li>
          <li class="toc__item"><span>Garantierte Farben</span><span>10</span></li>
          <li class="toc__item"><span>Natürlich der Umwelt zuliebe</span><span>10</span></li>
        </ul>
      </nav>
      <span class="folio folio--left">2</span>
    </section>

    <section class="page page--right">
      <div class="content">
        <h1 class="content__title">Fachlatein für Fortgeschrittene</h1>
        <p class="content__lead">Die gebräuchlichsten Fachbegriffe und Abkürzungen</p>
        <dl class="glossary">
          <dt>ungestrichen</dt>
          <dd>Unveredelte, maschinenglatte oder satinierte Papiere, die aus verschiedenen Faserstoffen hergestellt werden können.</dd>
          <dt>satiniert/<br>scharf satiniert</dt>
          <dd>In einem Kalander nachträglich und unterschiedlich stark geglättete Papiere.</dd>
          <dt>gestrichen</dt>
          <dd>Die Oberfläche des Papiers wird bereits in der Papiermaschine oder nachträglich in einer Streichmaschine durch einen Strichauftrag veredelt. Daraus ergibt sich eine bessere Druckwiedergabe.</dd>
          <dt>matt gestrichen</dt>
          <dd>Die Oberfläche des Papiers wird in einem zusätzlichen Arbeitsgang mit matten Pigmenten gestrichen.</dd>
          <dt>halbmatt gestrichen/<br>gestrichen (silk/satin)</dt>
          <dd>Ein besonderer Strichauftrag und/oder spezielles Kalandrieren erzeugen eine halbmatte Oberfläche.</dd>
          <dt>glänzend gestrichen</dt>
          <dd>Durch nachträgliches Satinieren und einen speziellen Strichauftrag entsteht eine glänzende Oberfläche.</dd>
          <dt>FCO</dt>
          <dd>In der Papiermaschine (inline) gestrichenes Papier mit matter oder glänzender Oberfläche.</dd>
        </dl>
        <div class="abbr">
          <p class="abbr__title">Abkürzungen und ihre Übersetzung</p>
          <table class="abbr__table">
            <tr><td>WFU</td><td>woodfree, uncoated</td><td>holzfrei ungestrichen</td></tr>
            <tr><td>MFS</td><td>machine-finished special</td><td>holzhaltig, maschinenglatt, ungestrichen</td></tr>
            <tr><td>WFC</td><td>woodfree, coated</td><td>holzfrei gestrichen</td></tr>
            <tr><td>MWC</td><td>middleweight, coated</td><td>doppelt gestrichen, holzhaltig, hoher Weißgrad, mittleres Gewicht</td></tr>
            <tr><td>LWC</td><td>lightweight, coated</td><td>einfach gestrichen, holzhaltig</td></tr>
            <tr><td>ULWC</td><td>ultralightweight, coated</td><td>einfach gestrichen, holzhaltig, ultraleichtgewichtig</td></tr>
            <tr><td>MFC</td><td>machine-finished, coated</td><td>maschinenglatt gestrichen, holzhaltig</td></tr>
            <tr><td>SC-A PLUS</td><td>supercalendered, brightwhite</td><td>superkalandriert, holzhaltig, hoher Weißgrad</td></tr>
            <tr><td>SC-A</td><td>supercalendered</td><td>superkalandriert, holzhaltig, Standard</td></tr>
            <tr><td>SC-B</td><td>softcalendered</td><td>softkalandriert, holzhaltig</td></tr>
            <tr><td>FCO</td><td>film coated offset</td><td>in der Papiermaschine (inline) gestrichenes Papier</td></tr>
            <tr><td>HSWO</td><td>heatset web offset</td><td>Rollenoffset mit Heißlufttrocknung</td></tr>
          </table>
        </div>
      </div>
      <span class="running-foot">PAPER &amp; PRINT</span>
      <span class="brand-name">Kumet</span>
      <span class="folio folio--right">3</span>
    </section>
  </div>
</body>
</html>
```